Product labels for new supplements business targeting high performing creative people

I need a label design for different supplements like Whey, BCAA, Melatonin etc. that I could customize for each use case separately.

The brand is called lanternfolk.life, and it would be the first design of the labels. We haven't sold any products yet, but the target audience is people with growth mindset, people who want to be as efficient as possible and are constantly looking to improve their lifestyle. As part of that, they are also working out, but don't know much about supplements yet. Mostly people between 20-34.

I don't have a too specific idea of the expected design, though it should be light, warm, smart and minimalist, maybe have some patterns. It should looks smart and clean (and expensive). Orange and golden might be the additional colors for white. I have attached the templates of some products that I plan to sell and also the logo of the brand.

Here's what I have used for inspiration:
Brands that I like and are somewhat similar in concept: https://www.vimqera.com/ (!!specially the way they
bring "how the product helps them" in focus, not "what the product is" & https://www.pobri.care/ &
https://www.selvoda.com/sport/ & https://en.kambelo.fr/ &
https://gridmarket.com/profiles/corawellhaldesign/designs/417586

Here's how different products look like: https://prodaxel.com/catalog

Target Market(s)

target audience is people with growth mindset, people who want to be as efficient as possible and are constantly looking to improve their lifestyle. As part of that, they are also working out, but don't know much about supplements yet. Mostly people between 20-34.

Industry/Entity Type

Supplements

Font styles to use
Sans Serif

Colors
FFC000
F8CF3A
FAE287
FDF2CF
FEFAEE
F0912C
F2A743
F7CA91
FBE8D2
FDF5EE
EE7325
F08F49
F5BC92
FAE3D3
FDF4ED

Requirements
Must have
• Clean, smart and minimalist design that can be applied for different products in different sizes, like Whey protein, BCAA, vitamins etc. available here: https://prodaxel.com/catalog
Nice to have
• Patterns, expensive look
Should not have
• Doodles, too many colors

```html
<!DOCTYPE html>
<html lang="en">
<head>
<meta charset="utf-8">
<title>lanternfolk.life – BCCA Powder label</title>
<link rel="stylesheet" href="https://fonts.googleapis.com/css2?family=Arimo:wght@400;700&display=swap">
<style>
  :root {
    --page-bg: #f3f3f3;
    --label-bg: #ffffff;
    --brand-orange: #ee7325;
    --accent-orange: #e84f0c;
    --tile-top: #f08f2c;
    --tile-bottom: #f2a743;
    --text-grey: #77787b;
  }
  * { margin: 0; padding: 0; box-sizing: border-box; }
  html, body {
    width: 1200px;
    height: 1200px;
    overflow: hidden;
    background: var(--page-bg);
    font-family: "Arimo", Arial, sans-serif;
  }
  .label {
    position: absolute;
    left: 215px;
    top: 185px;
    width: 770px;
    height: 830px;
    background: var(--label-bg);
    box-shadow: 0 10px 40px rgba(0,0,0,0.06);
  }
  .label__category {
    position: absolute;
    left: 80px;
    top: 0;
    height: 830px;
    display: flex;
    align-items: center;
    writing-mode: vertical-rl;
    transform: rotate(180deg);
    font-size: 69px;
    font-weight: 400;
    letter-spacing: 0.5px;
    color: var(--text-grey);
    line-height: 1;
  }
  .brand-tile {
    position: absolute;
    left: 232px;
    top: 0;
    width: 328px;
    height: 282px;
    border-radius: 0 0 26px 26px;
    background: linear-gradient(135deg, var(--tile-top), var(--tile-bottom));
  }
  .brand-name {
    position: absolute;
    left: 205px;
    top: 290px;
    width: 382px;
    text-align: center;
    font-size: 54px;
    font-weight: 400;
    color: var(--text-grey);
    line-height: 1;
  }
  .product-name {
    position: absolute;
    left: 168px;
    top: 418px;
    font-size: 168px;
    font-weight: 700;
    color: var(--accent-orange);
    line-height: 1;
    letter-spacing: -2px;
  }
  .product-form {
    position: absolute;
    left: 172px;
    top: 578px;
    font-size: 98px;
    font-weight: 400;
    color: var(--text-grey);
    line-height: 1;
  }
  .benefits {
    position: absolute;
    left: 345px;
    top: 680px;
    list-style: none;
    font-size: 20px;
    color: var(--accent-orange);
    line-height: 33px;
  }
  .net-weight {
    position: absolute;
    left: 345px;
    top: 752px;
    font-size: 50px;
    font-weight: 700;
    color: var(--text-grey);
    line-height: 1;
  }
</style>
</head>
<body>
  <main class="label">
    <div class="label__category">DIETARY SUPPLEMENT</div>
    <div class="brand-tile" aria-hidden="true"></div>
    <div class="brand-name">lanternfolk.life</div>
    <h1 class="product-name">BCCA</h1>
    <h2 class="product-form">POWDER</h2>
    <ul class="benefits">
      <li>Increases energy and stamina</li>
      <li>Helps reduce stress</li>
    </ul>
    <p class="net-weight">200g</p>
  </main>
</body>
</html>
```